'Tarovin' a financial/crypto-currency exchange in the middle east

On the card we need 1) Name 2) title 3) email address 4) phone number using the same colors and theme as the logo. On one side we just want the logo and we want the whole card to be in blue (same blue as logo) with the logo in the back being white.
Industry/Entity Type
Financial

```html
<!DOCTYPE html>
<html lang="en">
<head>
<meta charset="UTF-8">
<title>Tarovin Business Card</title>
<link href="https://fonts.googleapis.com/css2?family=Lato:wght@400;700;900&display=swap" rel="stylesheet">
<style>
  :root {
    --brand-blue: #0a90cc;
    --card-white: #ffffff;
    --backdrop: #eef0f2;
  }
  * { margin: 0; padding: 0; box-sizing: border-box; }
  html, body {
    width: 1200px; height: 900px; overflow: hidden;
    background: var(--backdrop);
    font-family: 'Lato', Arial, sans-serif;
  }
  .canvas { position: relative; width: 1200px; height: 900px; }

  .card { position: absolute; overflow: hidden; box-shadow: 0 6px 18px rgba(0,0,0,0.12); }

  /* Front: details side */
  .card-front {
    left: 178px; top: 74px; width: 588px; height: 364px;
    background: var(--brand-blue);
  }
  .front-shape { position: absolute; inset: 0; }
  .front-wordmark {
    position: absolute; left: 20px; top: 160px;
    font-weight: 900; font-size: 44px; color: var(--brand-blue);
    line-height: 1;
  }
  .identity {
    position: absolute; right: 37px; top: 50px; text-align: right;
    color: var(--card-white);
  }
  .identity-name { font-weight: 700; font-size: 21px; letter-spacing: 0.2px; line-height: 1.1; }
  .identity-title { font-weight: 400; font-size: 17px; margin-top: 2px; }

  .contacts {
    position: absolute; right: 37px; top: 256px;
    list-style: none; color: var(--card-white);
  }
  .contact-item {
    display: flex; align-items: center; justify-content: flex-end;
    gap: 6px; font-size: 16px; height: 21.5px;
  }
  .contact-icon { width: 19px; height: 19px; flex: none; }

  /* Back: brand side, all blue with white mark */
  .card-back {
    left: 388px; top: 505px; width: 567px; height: 352px;
    background: var(--brand-blue);
  }
  .brand-lockup {
    position: absolute; left: 118px; top: 126px;
    display: flex; align-items: center; gap: 18px;
  }
  .brand-circle { width: 98px; height: 98px; flex: none; }
  .brand-name {
    font-weight: 900; font-size: 56px; color: var(--card-white);
    line-height: 1;
  }
  .back-web {
    position: absolute; left: 0; right: 0; top: 284px; text-align: center;
    font-weight: 700; font-size: 18px; color: var(--card-white);
  }
</style>
</head>
<body>
<main class="canvas">

  <section class="card card-front" aria-label="Card front with contact details">
    <svg class="front-shape" width="588" height="364" viewBox="0 0 588 364" aria-hidden="true">
      <circle cx="68" cy="182" r="226" fill="#ffffff"/>
    </svg>
    <div class="front-wordmark">Tarovin</div>

    <div class="identity">
      <div class="identity-name">DANIEL HARPER</div>
      <div class="identity-title">Managing Director</div>
    </div>

    <ul class="contacts">
      <li class="contact-item">310 482 7719
        <svg class="contact-icon" viewBox="0 0 20 20" aria-hidden="true">
          <circle cx="10" cy="10" r="9" fill="none" stroke="#fff" stroke-width="1.4"/>
          <path d="M6 8.5c0-1.5 1.8-2.5 4-2.5s4 1 4 2.5l-1.6.4-.4-1.3H8l-.4 1.3z M7 10h6l1 4H6z" fill="#fff"/>
        </svg>
      </li>
      <li class="contact-item">hello@tarovin-mail.com
        <svg class="contact-icon" viewBox="0 0 20 20" aria-hidden="true">
          <circle cx="10" cy="10" r="9" fill="none" stroke="#fff" stroke-width="1.4"/>
          <rect x="5.5" y="6.5" width="9" height="7" fill="#fff"/>
          <path d="M5.5 6.5l4.5 4 4.5-4" fill="none" stroke="#0a90cc" stroke-width="1"/>
        </svg>
      </li>
      <li class="contact-item">www.tarovinexchange.com
        <svg class="contact-icon" viewBox="0 0 20 20" aria-hidden="true">
          <circle cx="10" cy="10" r="9" fill="none" stroke="#fff" stroke-width="1.4"/>
          <circle cx="10" cy="10" r="5.5" fill="#fff"/>
          <path d="M4.5 10h11M10 4.5c-2 2-2 9 0 11M10 4.5c2 2 2 9 0 11" fill="none" stroke="#0a90cc" stroke-width="0.9"/>
        </svg>
      </li>
    </ul>
  </section>

  <section class="card card-back" aria-label="Card back with brand name">
    <div class="brand-lockup">
      <svg class="brand-circle" viewBox="0 0 98 98" aria-hidden="true">
        <circle cx="49" cy="49" r="45" fill="none" stroke="#ffffff" stroke-width="6"/>
      </svg>
      <span class="brand-name">Tarovin</span>
    </div>
    <div class="back-web">www.tarovin.com</div>
  </section>

</main>
</body>
</html>
```